Portrait of a Graduate

Our school community has created a document which describes the characteristics that every student who graduates from our school should possess. We would like a visual graphic to present the information to parents\ community. We came up with three buckets (Personal, Social, and Academic) and the concept "BLH Graduates Will Be Okay" is the central theme.
We are open to 2 different concepts:
1. A ven diagram of sorts, where the three buckets are each in an area - and the over lap is "BLH Graduates Will Be Okay"
2. Our logo has a sassafras leaf in it - using the leaves to represent each bucket and the central concept as the stem - or some other creative version.

The text to be used is below:

BLH Graduates Will Be Okay (at the center/on the stem)

1. Personal
They will:
have self-worth
advocate for themselves
feel secure in their future

2. Social
They will:
embrace differences
engage in trusting relationships
be compassionate (members of their community)

3. Academic
They will:
apply skills and strategies
creatively problem-solve
achieve individual success

```html
<!DOCTYPE html>
<html lang="en">
<head>
<meta charset="utf-8">
<title>BLH Graduates Will Be Okay</title>
<link rel="stylesheet" href="https://fonts.googleapis.com/css2?family=Baloo+2:wght@800&family=Montserrat:wght@700&family=Open+Sans:ital,wght@1,700&family=Roboto+Condensed:wght@400&display=swap">
<style>
  :root {
    --yellow-deep: #eec23a;
    --yellow-mid: #f2cd52;
    --yellow-light: #f8df7c;
    --leaf-tone: #d9ad2e;
    --forest: #1f4a2b;
    --title-yellow: #f2c83c;
    --personal-top: #f08c70;
    --personal-bottom: #d04a3a;
    --personal-red: #e0262a;
    --social-top: #818b9b;
    --social-bottom: #2f3846;
    --social-ink: #2b3342;
    --academic-top: #6f9b7b;
    --academic-bottom: #5e8b6b;
    --academic-ink: #5f8e6b;
    --white: #ffffff;
  }
  html, body {
    margin: 0;
    padding: 0;
    overflow: hidden;
    background: var(--white);
  }
  .canvas {
    position: relative;
    width: 1200px;
    height: 848px;
    overflow: hidden;
    background: linear-gradient(100deg, var(--yellow-deep) 0%, var(--yellow-mid) 60%, var(--yellow-light) 100%);
  }
  .leaf-decoration {
    position: absolute;
    border-radius: 60% 40% 60% 40%;
    background: radial-gradient(circle at 50% 50%, var(--leaf-tone) 0%, rgba(217, 173, 46, 0) 70%);
    opacity: 0.55;
  }
  .leaf-decoration--left { left: -60px; top: -40px; width: 300px; height: 420px; }
  .leaf-decoration--right { right: -40px; top: -30px; width: 260px; height: 300px; }

  .headline {
    position: absolute;
    left: 0;
    top: 38px;
    width: 100%;
    margin: 0;
    text-align: center;
    font-family: "Baloo 2", "Arial Rounded MT Bold", sans-serif;
    font-weight: 800;
    font-size: 66px;
    line-height: 1;
    letter-spacing: 2px;
    color: var(--forest);
  }
  .banner {
    position: absolute;
    left: 366px;
    top: 140px;
    width: 574px;
    height: 90px;
    background: var(--forest);
    border-radius: 14px 30px 10px 36px / 20px 14px 28px 12px;
    transform: rotate(-1deg);
  }
  .banner__text {
    position: absolute;
    left: 0;
    top: 140px;
    width: 100%;
    height: 90px;
    display: flex;
    align-items: center;
    justify-content: center;
    font-family: "Baloo 2", "Arial Rounded MT Bold", sans-serif;
    font-weight: 800;
    font-style: italic;
    font-size: 64px;
    letter-spacing: 4px;
    color: var(--title-yellow);
    transform: skewX(-8deg);
  }

  .pillar {
    position: absolute;
    top: 384px;
    height: 464px;
  }
  .pillar--personal { left: 0; width: 400px; background: linear-gradient(180deg, var(--personal-top), var(--personal-bottom)); }
  .pillar--social { left: 400px; width: 400px; background: linear-gradient(180deg, var(--social-top), var(--social-bottom)); }
  .pillar--academic { left: 800px; width: 400px; background: linear-gradient(180deg, var(--academic-top), var(--academic-bottom)); }

  .badges {
    position: absolute;
    left: 0;
    top: 0;
    width: 1200px;
    height: 848px;
  }

  .pillar__label {
    position: absolute;
    top: 146px;
    left: 0;
    height: 54px;
    display: flex;
    align-items: center;
    padding-left: 38px;
    box-sizing: border-box;
    background: var(--white);
    border-radius: 0 27px 27px 0;
    font-family: "Montserrat", Arial, sans-serif;
    font-weight: 700;
    font-size: 38px;
    letter-spacing: 0.5px;
  }
  .pillar--personal .pillar__label { width: 286px; color: var(--personal-red); }
  .pillar--social .pillar__label { width: 220px; color: var(--social-ink); padding-left: 36px; }
  .pillar--academic .pillar__label { width: 286px; color: var(--academic-ink); padding-left: 32px; }

  .pillar__lead {
    position: absolute;
    left: 40px;
    top: 220px;
    margin: 0;
    font-family: "Open Sans", Arial, sans-serif;
    font-weight: 700;
    font-style: italic;
    font-size: 32px;
    color: var(--white);
  }
  .pillar__traits {
    position: absolute;
    left: 34px;
    top: 272px;
    margin: 0;
    padding: 0;
    list-style: none;
    font-family: "Roboto Condensed", "Arial Narrow", sans-serif;
    font-size: 25px;
    line-height: 43px;
    color: var(--white);
  }
  .pillar__traits li {
    position: relative;
    padding-left: 26px;
  }
  .pillar__traits li::before {
    content: "";
    position: absolute;
    left: 0;
    top: 18px;
    width: 8px;
    height: 8px;
    border-radius: 50%;
    background: var(--white);
  }
</style>
</head>
<body>
<main class="canvas">
  <div class="leaf-decoration leaf-decoration--left" role="img" aria-label="Faint sassafras leaf decoration"></div>
  <div class="leaf-decoration leaf-decoration--right" role="img" aria-label="Faint sassafras leaf decoration"></div>

  <h1 class="headline">BLH GRADUATES</h1>
  <div class="banner"></div>
  <div class="banner__text">WILL BE OKAY</div>

  <section class="pillar pillar--personal">
    <div class="pillar__label">PERSONAL</div>
    <p class="pillar__lead">They will</p>
    <ul class="pillar__traits">
      <li>Have self-worth</li>
      <li>Advocate for themselves</li>
      <li>Feel secure in their future</li>
    </ul>
  </section>

  <section class="pillar pillar--social">
    <div class="pillar__label">SOCIAL</div>
    <p class="pillar__lead">They will</p>
    <ul class="pillar__traits">
      <li>Embrace differences</li>
      <li>Engage in trusting relationships</li>
      <li>Be compassionate</li>
    </ul>
  </section>

  <section class="pillar pillar--academic">
    <div class="pillar__label">ACADEMIC</div>
    <p class="pillar__lead">They will</p>
    <ul class="pillar__traits">
      <li>Apply skills and strategies</li>
      <li>Creatively problem-solve</li>
      <li>Achieve individual success</li>
    </ul>
  </section>

  <svg class="badges" viewBox="0 0 1200 848" aria-hidden="true">
    <defs>
      <linearGradient id="badge-personal" x1="0" y1="0" x2="1" y2="0">
        <stop offset="0" stop-color="#d2302a"/>
        <stop offset="1" stop-color="#f2937a"/>
      </linearGradient>
      <linearGradient id="badge-social" x1="0" y1="0" x2="1" y2="0">
        <stop offset="0" stop-color="#27303f"/>
        <stop offset="1" stop-color="#8f99aa"/>
      </linearGradient>
      <linearGradient id="tab-yellow" x1="0" y1="0" x2="0" y2="1">
        <stop offset="0" stop-color="#f1ca4a"/>
        <stop offset="1" stop-color="#f4d560"/>
      </linearGradient>
    </defs>

    <g class="badge-tabs" fill="url(#tab-yellow)" stroke="url(#tab-yellow)" stroke-width="28" stroke-linejoin="round">
      <polygon points="189,252 307,316 307,444 189,508 71,444 71,316"/>
      <polygon points="592,252 710,316 710,444 592,508 474,444 474,316"/>
      <polygon points="992,252 1110,316 1110,444 992,508 874,444 874,316"/>
    </g>

    <g class="badge-hexes" stroke-width="18" stroke-linejoin="round">
      <polygon points="189,262 279,312 279,412 189,462 99,412 99,312" fill="url(#badge-personal)" stroke="url(#badge-personal)"/>
      <polygon points="592,262 682,312 682,412 592,462 502,412 502,312" fill="url(#badge-social)" stroke="url(#badge-social)"/>
      <polygon points="992,262 1082,312 1082,412 992,462 902,412 902,312" fill="#638f6e" stroke="#638f6e"/>
    </g>

    <g class="icon-person" fill="#ffffff">
      <circle cx="189" cy="334" r="13"/>
      <path d="M170 396 V366 a19 19 0 0 1 38 0 V396 Z"/>
    </g>

    <g class="icon-group" fill="#ffffff">
      <circle cx="558" cy="348" r="7"/>
      <path d="M548 388 V370 a10 10 0 0 1 20 0 V388 Z"/>
      <circle cx="626" cy="348" r="7"/>
      <path d="M616 388 V370 a10 10 0 0 1 20 0 V388 Z"/>
      <circle cx="575" cy="342" r="9"/>
      <path d="M563 394 V368 a12 12 0 0 1 24 0 V394 Z"/>
      <circle cx="609" cy="342" r="9"/>
      <path d="M597 394 V368 a12 12 0 0 1 24 0 V394 Z"/>
      <circle cx="592" cy="334" r="11"/>
      <path d="M577 398 V362 a15 15 0 0 1 30 0 V398 Z"/>
    </g>

    <g class="icon-book" fill="#ffffff">
      <path d="M948 336 Q970 330 988 340 V392 Q970 384 948 388 Z"/>
      <path d="M1036 336 Q1014 330 996 340 V392 Q1014 384 1036 388 Z"/>
      <path d="M942 344 V398 Q968 392 992 400 Q1016 392 1042 398 V344 H1038 V392 Q1014 388 992 396 Q970 388 946 392 V344 Z"/>
    </g>
  </svg>
</main>
</body>
</html>
```